Electronic Refurbishment Warehouse needs a Website

We are looking for a clean, professional looking design with iconic imagery. Our main point we want to get across is that we will help clients save time, and money, and provide outstanding quality. Our logo can be found in the uploads section. This site is used to impress clients that we have a pre-existing relationship with. This site will be available for the public but it will not be used to advertise to the public or to drive traffic to it. The color scheme we are looking to stay with is blue, but that is not to say that everything should be a shade of blue. Last note, see site map below.

Site Map:

Home
Company
a. company overview
b. CEO letter
Services
a. Remanufacture & Refurbishment Services
1. Consumer Electronics
2. Cellular Phones
b.Reverse Logistics Management
c.Warranty Repair & Field Services
d.Quality Control & Assurance
e.Warehousing & Distribution
Careers
Contact Us

Reason: We want to allocate more time for designers to do what they do best.

Target Market(s)

Phone and TV Retailers that may have units that need to be refurbished. Example Velorin, tallcart, qvo, etc.

Industry/Entity Type

Electronics

Requirements
Must have
• Home Page Slider.
Iconic imagery and navigation.
The ability to be put into the 960 Grid.

```html
<!DOCTYPE html>
<html lang="en">
<head>
<meta charset="utf-8">
<title>Norvane Group – Reverse Logistics Management</title>
<link rel="stylesheet" href="https://fonts.googleapis.com/css2?family=Cinzel:wght@400&family=Arimo:ital,wght@0,400;0,700;1,700&display=swap">
<style>
:root{
  --navy:#0a4a86;
  --navy-dark:#053563;
  --blue:#0f5fa6;
  --blue-mid:#1a6fb8;
  --title-blue:#0d4a8c;
  --green:#5a9a12;
  --green-dark:#3f7a08;
  --text:#1c1c1c;
  --panel:#f6f6f6;
  --sidebar:#e6e6e6;
  --input:#c9c9c9;
  --white:#ffffff;
}
*{box-sizing:border-box;margin:0;padding:0}
html,body{width:1057px;height:1200px;overflow:hidden;background:var(--white)}
body{position:relative;font-family:"Arimo",Arial,sans-serif;color:var(--text)}
.abs{position:absolute}

/* header */
.top-rule{left:0;top:0;width:1057px;height:4px;background:var(--navy-dark)}
.site-header{left:0;top:4px;width:1057px;height:100px;background:linear-gradient(#ffffff 0%,#f4f4f4 55%,#d6d6d6 100%);border-bottom:1px solid #bcbcbc}
.brand{left:76px;top:34px;display:flex;align-items:center;gap:10px;font-size:26px;font-weight:700;color:var(--blue)}
.brand-mark{width:40px;height:40px;background:var(--blue)}
.main-nav a{position:absolute;top:43px;height:28px;line-height:28px;border-radius:14px;text-align:center;font-size:13.5px;font-weight:700;color:#111;text-decoration:none;background:linear-gradient(#ffffff,#ececec);border:1px solid #dcdcdc}
.main-nav a.is-current{background:var(--navy);color:var(--white);border-color:var(--navy)}

/* hero */
.hero{left:0;top:104px;width:1057px;height:357px;background:radial-gradient(ellipse at 55% 20%,#2b7cc4 0%,#1260a8 40%,#0a4d8f 100%)}
.hero-title{left:70px;top:142px;font-family:"Cinzel",Georgia,serif;font-size:50px;line-height:58px;color:var(--white);text-shadow:0 2px 3px rgba(0,0,0,.45);letter-spacing:.5px}
.hero-list{left:90px;top:287px;list-style:none}
.hero-list li{display:flex;align-items:center;gap:9px;height:33px;font-size:17px;color:var(--white)}
.hero-list svg{width:18px;height:16px}
.btn-learn{left:479px;top:364px;width:154px;height:46px;border-radius:4px;background:linear-gradient(#79b92a,#3f8010);border:1px solid #2f6a08;color:var(--white);font-size:22px;font-weight:700;text-align:center;line-height:44px;text-shadow:0 1px 2px rgba(0,0,0,.5)}
.hero-art{left:691px;top:155px;width:289px;height:247px;border-radius:8px;background:radial-gradient(circle at 40% 45%,#ffffff 0%,#e3e3e3 40%,#d84444 70%,rgba(19,96,168,0) 100%)}

/* feature panel */
.feature{left:60px;top:483px;width:638px;height:258px;background:var(--panel)}
.feature-title{left:78px;top:502px;font-size:31px;color:var(--title-blue)}
.feature-rule{left:60px;top:552px;width:638px;border-top:1px dashed #dadada}
.feature-art{left:76px;top:574px;width:196px;height:147px;background:radial-gradient(circle,#e4ecf6 0%,#ffffff 75%);border:1px solid #e5e5e5}
.body-copy{font-size:13.3px;line-height:16.5px;color:var(--text)}
.body-copy p+p{margin-top:16px}
.feature-copy{left:291px;top:582px;width:375px}
.link-more{font-size:13.5px;font-weight:700;font-style:italic;color:#1a1a1a;text-decoration:none}
.feature-more{left:596px;top:708px}

/* columns */
.col-icon{width:58px;height:62px}
.col-title{font-size:25px;line-height:30px;color:var(--title-blue)}
.col-title span{color:var(--green)}
.col-more{color:var(--green-dark)}
.col-divider{left:366px;top:795px;height:268px;border-left:1px solid #dedede}

/* sidebar */
.quote-icon{left:722px;top:483px;width:50px;height:52px;background:linear-gradient(#f0f0f0,#bcbcbc);border-radius:3px}
.quote-title{left:780px;top:495px;font-size:24px;font-weight:700;color:var(--green)}
.quote-box{left:718px;top:542px;width:271px;height:314px;border-radius:8px;background:linear-gradient(#e9e9e9,#dcdcdc 60%,#eeeeee)}
.field-label{left:743px;font-size:13px;color:#111}
.field{left:737px;width:226px;height:38px;border-radius:8px;background:var(--input)}
.btn-submit{left:792px;top:798px;width:129px;height:41px;border-radius:4px;background:linear-gradient(#3a3a3a,#000);color:var(--white);font-size:25px;text-align:center;line-height:41px}
.follow-box{left:717px;top:876px;width:272px;height:181px;border-radius:8px;background:linear-gradient(#ffffff,#f4f4f4);border:1px solid #e8e8e8}
.follow-title{left:740px;top:900px;font-size:24px;font-weight:700;color:#111;border-bottom:1.5px solid #111;line-height:27px}
.social{top:949px;width:38px;height:38px;border-radius:4px;background:var(--blue)}

/* footer */
.site-footer{left:0;top:1092px;width:1057px;height:108px;background:linear-gradient(var(--navy-dark),#0b5aa0);border-top:4px solid #033360}
.footer-links{left:0;width:1057px;top:1126px;text-align:center;font-size:12.5px;color:var(--white)}
.footer-copy{left:0;width:1057px;top:1156px;text-align:center;font-size:12.5px;color:var(--white)}
</style>
</head>
<body>

<div class="abs top-rule"></div>
<header class="abs site-header"></header>
<div class="abs brand"><span class="brand-mark"></span>Norvane group</div>
<nav class="main-nav">
  <a class="is-current" style="left:424px;width:83px">HOME</a>
  <a style="left:521px;width:95px">COMPANY</a>
  <a style="left:640px;width:95px">SERVICES</a>
  <a style="left:760px;width:95px">CAREERS</a>
  <a style="left:876px;width:114px">CONTACT US</a>
</nav>

<section class="abs hero"></section>
<h1 class="abs hero-title">REVERSE LOGISTICS<br>MANAGEMENT</h1>
<ul class="abs hero-list">
  <li><svg viewBox="0 0 18 16"><path d="M1 9l5 5L17 2" fill="none" stroke="#f2e31a" stroke-width="3.5"/></svg>Remanufacture &amp; Refurbishment Services</li>
  <li><svg viewBox="0 0 18 16"><path d="M1 9l5 5L17 2" fill="none" stroke="#f2e31a" stroke-width="3.5"/></svg>Warranty Repair &amp; Field Services</li>
  <li><svg viewBox="0 0 18 16"><path d="M1 9l5 5L17 2" fill="none" stroke="#f2e31a" stroke-width="3.5"/></svg>Quality Control &amp; Assurance</li>
  <li><svg viewBox="0 0 18 16"><path d="M1 9l5 5L17 2" fill="none" stroke="#f2e31a" stroke-width="3.5"/></svg>Warehousing &amp; Distribution</li>
</ul>
<div class="abs btn-learn">Learn more</div>
<div class="abs hero-art" role="img" aria-label="3D illustration of white cubes with red spheres"></div>

<section class="abs feature"></section>
<h2 class="abs feature-title" style="font-weight:400">Warehousing and Distribution</h2>
<div class="abs feature-rule"></div>
<div class="abs feature-art" role="img" aria-label="Illustration of figures connected around a globe"></div>
<div class="abs body-copy feature-copy">
  <p>Lorem Ipsum is simply dummy text of the printing and typeset-ting industry.</p>
  <p>Lorem Ipsum has been the industry's standard dummy text ever since the 1500s, when an unknown printer took a galley of type and scrambled it to make a type specimen book.</p>
</div>
<a class="abs link-more feature-more">Learn More</a>

<svg class="abs col-icon" style="left:64px;top:798px" viewBox="0 0 58 62" aria-label="Tick icon" role="img">
  <rect x="4" y="38" width="36" height="18" rx="2" fill="#e2e2e2" stroke="#aaa"/>
  <path d="M8 30l12 18L54 4" fill="none" stroke="#d8161b" stroke-width="7" stroke-linecap="round"/>
</svg>
<h3 class="abs col-title" style="left:133px;top:799px;font-weight:400">Quality Control &amp;<br><span>Assurance</span></h3>
<div class="abs body-copy" style="left:70px;top:888px;width:250px">
  <p>Lorem Ipsum is simply dummy text of the printing and typesetting industry. Lorem Ipsum has been the industry's standard dummy text ever since the 1500s.</p>
  <p>when an unknown printer took a galley of type and scrambled it to make a type specimen book.</p>
</div>
<a class="abs link-more col-more" style="left:237px;top:1047px">Learn More</a>

<div class="abs col-divider"></div>

<div class="abs col-icon" style="left:399px;top:798px;width:55px;height:58px;background:#f4dc2c;border-radius:3px" role="img" aria-label="Sticky note with gears icon"></div>
<h3 class="abs col-title" style="left:473px;top:799px;font-weight:400">Warranty Repair &amp;<br><span>Services</span></h3>
<div class="abs body-copy" style="left:402px;top:888px;width:250px">
  <p>Lorem Ipsum is simply dummy text of the printing and typesetting industry. Lorem Ipsum has been the industry's standard dummy text ever since the 1500s.</p>
  <p>when an unknown printer took a galley of type and scrambled it to make a type specimen book.</p>
</div>
<a class="abs link-more col-more" style="left:578px;top:1047px">Learn More</a>

<div class="abs quote-icon" role="img" aria-label="Notepad and pencil icon"></div>
<h3 class="abs quote-title">Request a Quote</h3>
<form class="abs quote-box"></form>
<label class="abs field-label" style="top:572px">Enter Your Name</label>
<div class="abs field" style="top:592px"></div>
<label class="abs field-label" style="top:646px">Enter Your Email ID</label>
<div class="abs field" style="top:665px"></div>
<label class="abs field-label" style="top:720px">Enter Your Mobile Number</label>
<div class="abs field" style="top:740px"></div>
<div class="abs btn-submit">Submit</div>

<aside class="abs follow-box"></aside>
<h3 class="abs follow-title">Follow Us On:</h3>
<span class="abs social" style="left:745px" aria-label="Social link"></span>
<span class="abs social" style="left:806px" aria-label="Social link"></span>
<span class="abs social" style="left:866px" aria-label="Social link"></span>
<span class="abs social" style="left:923px" aria-label="Social link"></span>

<footer class="abs site-footer"></footer>
<p class="abs footer-links">Home | About Us | Services | Company | Careers | Contact Us | Jobs | Privacy Policy | Terms of Conditions</p>
<p class="abs footer-copy">© Copyright 2012 Norvane Group. All Rights Reserved</p>

</body>
</html>
```